Food manufacturer stationary
Business cards, envelopes, letterhead, cover sheet etc
Professional
Gustavo Arrieta
CEO
2875 North Clover Ave Salt Lake City, UT 84117
GUSTAVOJR@CORVANAFOODS.EXAMPLE
WWW.CORVANAMEXICANFOODS.EXAMPLE
Looking for something classy, professional, and modern. Something that says to client holding card this is a well established strong company

```html
<!DOCTYPE html>
<html lang="en">
<head>
<meta charset="utf-8">
<title>Corvana Mexican Foods – Stationery Set</title>
<link rel="stylesheet" href="https://fonts.googleapis.com/css2?family=Cinzel:wght@700&family=Lato:wght@400;700&display=swap">
<style>
:root{
  --backdrop:#ebe5db;
  --paper:#ffffff;
  --brown:#3b2212;
  --brown-mid:#6b4322;
  --gold:#c8962e;
  --gold-light:#f0d48a;
  --ink:#4a3a2c;
  --label:#6d5f50;
  --bull:#efe7da;
}
*{box-sizing:border-box;margin:0;padding:0}
html,body{width:1200px;height:631px;overflow:hidden;background:var(--backdrop);font-family:"Lato",sans-serif;color:var(--ink)}
.sheet-set{position:relative;width:1200px;height:631px}
.item{position:absolute;background:var(--paper);box-shadow:0 2px 6px rgba(0,0,0,.25);overflow:hidden}
.label{position:absolute;font-size:7px;font-weight:700;color:var(--label);text-align:center;white-space:nowrap}
.swoosh{position:absolute;inset:0;width:100%;height:100%}
.brand{display:flex;align-items:center;gap:4px;position:absolute}
.brand-dot{border-radius:50%;background:var(--brown);border:1.5px solid var(--gold)}
.brand-name{font-family:"Cinzel",serif;font-weight:700;color:var(--brown);letter-spacing:.5px}
.brand.on-dark .brand-name{color:var(--gold-light)}
.bull-art{position:absolute;border-radius:40% 50% 30% 40%;background:radial-gradient(ellipse at 50% 45%,var(--bull) 0%,rgba(239,231,218,.55) 60%,rgba(255,255,255,0) 75%)}
.footer-text{position:absolute;left:0;right:0;text-align:center;font-size:4.5px;line-height:1.5;color:var(--ink)}
.person{position:absolute;font-size:5px;line-height:1.4}
.person strong{font-family:"Cinzel",serif;font-size:6px;color:var(--brown)}
.fax-title{position:absolute;left:254px;top:90px;width:40px;text-align:right;font-size:10px;font-weight:700;color:var(--brown)}
.fax-table{position:absolute;left:18px;top:106px;width:276px;border-collapse:collapse;font-size:5px}
.fax-table td{border:.6px solid #b9aa96;height:15px;padding:2px 3px;vertical-align:top}
.fax-checks{position:absolute;left:18px;top:176px;display:flex;gap:14px;font-size:5px}
.fax-checks span::before{content:"";display:inline-block;width:5px;height:5px;border:.6px solid var(--ink);margin-right:3px;vertical-align:-1px}
</style>
</head>
<body>
<main class="sheet-set">

  <!-- Business cards -->
  <div class="label" style="left:12px;top:12px;width:125px">Business Card Front</div>
  <section class="item business-card card-front" style="left:12px;top:24px;width:125px;height:77px">
    <svg class="swoosh" viewBox="0 0 125 77" preserveAspectRatio="none"><path d="M0 58 Q60 48 125 68 V77 H0Z" fill="var(--gold)"/><path d="M0 66 Q60 58 125 74 V77 H0Z" fill="var(--brown)"/></svg>
    <div class="brand" style="left:34px;top:8px"><span class="brand-dot" style="width:8px;height:8px"></span><span class="brand-name" style="font-size:8px">Corvana</span></div>
    <div class="person" style="left:10px;top:26px"><strong>Gustavo Arrieta</strong><br>CEO<br>2875 North Clover Ave, Salt Lake City, UT 84117<br>GUSTAVOJR@CORVANAFOODS.EXAMPLE</div>
  </section>

  <div class="label" style="left:149px;top:12px;width:127px">Business Card Option 1 (Back)</div>
  <section class="item business-card card-back-one" style="left:149px;top:24px;width:127px;height:77px">
    <svg class="swoosh" viewBox="0 0 127 77" preserveAspectRatio="none"><path d="M60 0 H127 V77 H40 Q95 40 60 0Z" fill="var(--brown)"/><path d="M60 0 Q95 40 40 77 H48 Q102 40 68 0Z" fill="var(--gold)"/></svg>
    <div class="brand" style="left:12px;top:33px"><span class="brand-dot" style="width:8px;height:8px"></span><span class="brand-name" style="font-size:8px">Corvana</span></div>
  </section>

  <div class="label" style="left:288px;top:12px;width:132px">Business Card Option 2 (Back)</div>
  <section class="item business-card card-back-two" style="left:288px;top:24px;width:132px;height:77px;background:linear-gradient(135deg,var(--brown-mid),var(--gold) 45%,var(--gold-light) 60%,var(--gold))">
    <div class="brand on-dark" style="left:34px;top:32px"><span class="brand-dot" style="width:10px;height:10px"></span><span class="brand-name" style="font-size:11px">Corvana</span></div>
  </section>

  <div class="label" style="left:439px;top:12px;width:137px">Business Card Option 3 (Back)</div>
  <section class="item business-card card-back-three" style="left:439px;top:24px;width:137px;height:77px">
    <svg class="swoosh" viewBox="0 0 137 77" preserveAspectRatio="none"><path d="M90 0 H137 V77 H110 Q130 40 90 0Z" fill="var(--gold)"/><path d="M108 0 H137 V77 H124 Q140 40 108 0Z" fill="var(--brown)"/></svg>
    <div class="brand" style="left:30px;top:33px"><span class="brand-dot" style="width:8px;height:8px"></span><span class="brand-name" style="font-size:9px">Corvana</span></div>
  </section>

  <!-- Fax cover -->
  <div class="label" style="left:36px;top:180px;width:343px">Fax Letter</div>
  <section class="item fax-sheet" style="left:36px;top:192px;width:343px;height:427px">
    <svg class="swoosh" viewBox="0 0 343 427" preserveAspectRatio="none"><path d="M300 0 H343 V427 H330 Q355 200 300 0Z" fill="var(--brown)"/><path d="M292 0 Q345 200 322 427 H330 Q355 200 300 0Z" fill="var(--gold)"/></svg>
    <div class="brand" style="left:135px;top:16px"><span class="brand-dot" style="width:12px;height:12px"></span><span class="brand-name" style="font-size:13px">Corvana</span></div>
    <div class="fax-title">FAX</div>
    <table class="fax-table">
      <tr><td>To:</td><td>From:</td></tr>
      <tr><td>Fax:</td><td>Pages:</td></tr>
      <tr><td>Phone:</td><td>Date:</td></tr>
      <tr><td>Re:</td><td>CC:</td></tr>
    </table>
    <div class="fax-checks"><span>Urgent</span><span>For Review</span><span>Please Comment</span><span>Please Reply</span><span>Please Recycle</span></div>
    <div class="bull-art" role="img" aria-label="Faint bull silhouette watermark" style="left:20px;top:200px;width:170px;height:190px"></div>
    <div class="footer-text" style="bottom:10px;right:40px">2875 North Clover Ave, Salt Lake City, UT 84117<br>P (801) 555-0142 · GUSTAVOJR@CORVANAFOODS.EXAMPLE · WWW.CORVANAMEXICANFOODS.EXAMPLE</div>
  </section>

  <!-- Letterhead -->
  <div class="label" style="left:396px;top:180px;width:336px">Letterhead</div>
  <section class="item letterhead" style="left:396px;top:192px;width:336px;height:427px">
    <svg class="swoosh" viewBox="0 0 336 427" preserveAspectRatio="none"><path d="M294 0 H336 V427 H324 Q348 200 294 0Z" fill="var(--brown)"/><path d="M286 0 Q338 200 316 427 H324 Q348 200 294 0Z" fill="var(--gold)"/></svg>
    <div class="brand" style="left:132px;top:16px"><span class="brand-dot" style="width:12px;height:12px"></span><span class="brand-name" style="font-size:13px">Corvana</span></div>
    <div class="bull-art" role="img" aria-label="Faint bull silhouette watermark" style="left:20px;top:110px;width:200px;height:230px"></div>
    <div class="footer-text" style="bottom:10px;right:40px">2875 North Clover Ave, Salt Lake City, UT 84117<br>P (801) 555-0142 · GUSTAVOJR@CORVANAFOODS.EXAMPLE · WWW.CORVANAMEXICANFOODS.EXAMPLE</div>
  </section>

  <!-- Envelopes -->
  <div class="label" style="left:749px;top:17px;width:432px">Envelope (Front)</div>
  <section class="item envelope-front" style="left:749px;top:29px;width:432px;height:175px">
    <svg class="swoosh" viewBox="0 0 432 175" preserveAspectRatio="none"><path d="M330 175 Q400 120 432 40 V175Z" fill="var(--brown)"/><path d="M300 175 Q390 130 432 30 V45 Q400 125 330 175Z" fill="var(--gold)"/></svg>
    <div class="brand" style="left:18px;top:18px"><span class="brand-dot" style="width:12px;height:12px"></span><span class="brand-name" style="font-size:13px">Corvana</span></div>
    <div class="person" style="left:30px;top:38px;font-size:4.5px">2875 North Clover Ave<br>Salt Lake City, UT 84117</div>
  </section>

  <div class="label" style="left:749px;top:279px;width:432px">Envelope Option 2 (Back)</div>
  <section class="item envelope-back-two" style="left:749px;top:290px;width:432px;height:140px">
    <svg class="swoosh" viewBox="0 0 432 140" preserveAspectRatio="none"><path d="M0 0 H432 L216 75Z" fill="#f7f3ec" stroke="#d9cfbf" stroke-width=".8"/><path d="M0 0 H432 L216 22Z" fill="var(--gold)" opacity=".6"/></svg>
    <div class="brand" style="left:180px;top:60px"><span class="brand-dot" style="width:9px;height:9px"></span><span class="brand-name" style="font-size:10px">Corvana</span></div>
  </section>

  <div class="label" style="left:749px;top:434px;width:432px">Envelope Option 3 (Back)</div>
  <section class="item envelope-back-three" style="left:749px;top:444px;width:432px;height:168px">
    <svg class="swoosh" viewBox="0 0 432 168" preserveAspectRatio="none"><defs><linearGradient id="flap-gold" x1="0" x2="1"><stop offset="0" stop-color="var(--gold)"/><stop offset=".5" stop-color="var(--gold-light)"/><stop offset="1" stop-color="var(--gold)"/></linearGradient></defs><path d="M0 0 H432 V30 L216 95 L0 30Z" fill="url(#flap-gold)"/><path d="M0 0 H432 V22 L216 82 L0 22Z" fill="var(--brown)"/></svg>
    <div class="brand on-dark" style="left:176px;top:36px"><span class="brand-dot" style="width:10px;height:10px"></span><span class="brand-name" style="font-size:11px">Corvana</span></div>
  </section>

</main>
</body>
</html>
```